Dalsten-Ko Photography needs a poster for a upcoming event

We need a Music Concert Poster designed for a musician named Marcus T. Linden. The concert is happening 6:30 pm, Saturday, January 10, 2015 Look to our current design ideas for inspiration. Keep it clean and simple but I want to see your creative ideas. Please view the throw togethers screenshots I have included in this project and then use one of the clean images in your design. Visit www.pinboardly.example/marclind/concert-posters/ for the musicians favorite music posters and gather ideas from there as well.

Requirements
Nice to have
• Lets tend to lean towards a more sanserif font

```html
<!DOCTYPE html>
<html lang="en">
<head>
<meta charset="utf-8">
<title>Marcus T. Linden in Concert</title>
<link rel="stylesheet" href="https://fonts.googleapis.com/css2?family=Open+Sans:wght@400;600;700&family=EB+Garamond:ital@1&display=swap">
<style>
  :root {
    --page: #ffffff;
    --ink: #333333;
    --ink-soft: #3c3c3c;
    --accent: #7a2b35;
    --disc: rgba(236, 229, 204, 0.88);
    --band: #3a3a3a;
    --photo-light: #d9d9d9;
    --photo-mid: #a8a8a8;
    --photo-dark: #2e2e2e;
    --portrait-deep: #1a1a1a;
    --portrait-tone: #6e6e6e;
  }
  * { margin: 0; padding: 0; box-sizing: border-box; }
  html, body { width: 1200px; height: 1000px; overflow: hidden; background: var(--page); }
  .poster {
    position: absolute; left: 17px; top: 143px; width: 1166px; height: 714px;
    overflow: hidden;
  }
  .poster__photo {
    position: absolute; inset: 0;
    background:
      radial-gradient(ellipse 520px 420px at 260px 300px, rgba(245,245,245,0.9), rgba(245,245,245,0) 70%),
      radial-gradient(ellipse 300px 500px at 1080px 200px, rgba(40,40,40,0.7), rgba(40,40,40,0) 75%),
      linear-gradient(90deg, var(--photo-light) 0%, #c4c4c4 35%, var(--photo-mid) 55%, #8a8a8a 70%, #5a5a5a 100%);
  }
  .poster__portrait {
    position: absolute; left: 560px; top: 0; width: 606px; height: 714px;
    background:
      radial-gradient(ellipse 170px 210px at 240px 300px, rgba(150,150,150,0.55), rgba(150,150,150,0) 80%),
      radial-gradient(ellipse 150px 120px at 240px 110px, rgba(30,30,30,0.85), rgba(30,30,30,0) 85%),
      radial-gradient(ellipse 330px 330px at 330px 720px, var(--portrait-deep), rgba(26,26,26,0) 90%),
      linear-gradient(100deg, rgba(110,110,110,0) 0%, rgba(60,60,60,0.35) 55%, rgba(30,30,30,0.6) 100%);
  }
  .poster__band {
    position: absolute; left: 0; right: 0; bottom: 0; height: 17px; background: var(--band);
  }
  .disc {
    position: absolute; border-radius: 50%; background: var(--disc);
  }
  .disc--title { left: 152px; top: 70px; width: 250px; height: 250px; }
  .disc--entry { left: 152px; top: 632px; width: 250px; height: 250px; }
  .headline {
    position: absolute; left: 74px; top: 112px;
    font-family: "Open Sans", sans-serif; font-weight: 600; font-size: 54px;
    letter-spacing: 0; color: var(--ink-soft); line-height: 1; white-space: nowrap;
  }
  .headline__rule { position: absolute; left: 161px; top: 198px; }
  .subtitle, .label {
    font-family: "EB Garamond", serif; font-style: italic; color: var(--accent);
  }
  .subtitle {
    position: absolute; left: 127px; top: 220px; width: 300px; text-align: center;
    font-size: 42px; line-height: 1;
  }
  .details {
    position: absolute; left: 27px; top: 330px; width: 500px; text-align: center;
    font-family: "Open Sans", sans-serif; color: var(--ink);
  }
  .label { font-size: 26px; line-height: 1; margin-bottom: 6px; }
  .value { font-weight: 700; font-size: 29px; line-height: 1.1; margin-bottom: 14px; white-space: nowrap; }
  .value__sep { color: #d8c98f; font-weight: 400; }
  .venue { font-weight: 700; font-size: 18px; line-height: 1.6; margin-top: 8px; }
  .address { font-size: 16.5px; line-height: 1.75; }
  .entry {
    position: absolute; left: 127px; top: 650px; width: 300px; text-align: center;
    font-family: "Open Sans", sans-serif; font-weight: 700; font-size: 16px;
    color: var(--accent); letter-spacing: 0.3px;
  }
</style>
</head>
<body>
  <main class="poster">
    <div class="poster__photo" role="img" aria-label="Black and white photograph of a softly blurred forest path"></div>
    <div class="poster__portrait" role="img" aria-label="Portrait of the musician in a dark shirt, looking back over his shoulder with a guitar resting on it"></div>
    <div class="disc disc--title"></div>
    <div class="disc disc--entry"></div>
    <h1 class="headline">MARCUS T. LINDEN</h1>
    <svg class="headline__rule" width="232" height="14" viewBox="0 0 232 14" aria-hidden="true">
      <line x1="2" y1="7" x2="230" y2="7" stroke="#333" stroke-width="1.5"/>
      <circle cx="116" cy="7" r="3" fill="#333"/>
    </svg>
    <p class="subtitle">in concert</p>
    <section class="details">
      <p class="label">- date -</p>
      <p class="value">Saturday, January 10<span class="value__sep"> | </span>2015</p>
      <p class="label">- time -</p>
      <p class="value">6:30 PM</p>
      <p class="label">- location -</p>
      <p class="venue">Harbor Pines Community Church</p>
      <p class="address">482 Larkspur Ave.<br>Seabrook Cove, Fl, 32590</p>
    </section>
    <p class="entry">- FREE ENTRANCE -</p>
    <div class="poster__band"></div>
  </main>
</body>
</html>
```